Flyer for annual KESTREL SUMMIT 2020

I would like a church event flyer designed. The event is called "KESTREL SUMMIT 2020". I am looking for a professional, yet catchy design that uses our brand colors and logo creatively while communicating key information of the event effectively.

1. The logo is attached in two color formats. The designer has the choice to use them as he/she want.

2. The location of the event is: Harlow Community Center, 239 Fennimore Street, Portland, ME 04117

3. Time and date of event. The designer can organize and format the date and time as he/she pleases.
Thursday December 31st @ 6:30PM
Friday January 1st @ 6:30PM
Saturday 2nd @ 6:30PM
Sunday 3rd @ 4:30PM

4. The topic of the event is "In Fire and On Fire". The designer is free to use this phrase as he/she pleases to create a good composition.

5. Speaker: Prophet Marcus Olunde (2 pictures of the speaker to choose from are attached)

6. Contact information: contact@brightmeadowfold.org - Telephone number: 207 583 2914

7. I would also like the following three words on the flyer. These words describe the focus of the event: FIRE, REVIVAL, PROPHETIC

Target Market(s)

Young adults

Font styles to use
Sans Serif

Requirements
Must have
• Logo, speaker's picture
Should not have
• cross image, church image

```html
<!DOCTYPE html>
<html lang="en">
<head>
<meta charset="utf-8">
<title>Kestrel Summit 2020 Flyer</title>
<link href="https://fonts.googleapis.com/css2?family=Oswald:wght@500;700&family=Montserrat:wght@500;600;700;800&display=swap" rel="stylesheet">
<style>
  :root {
    --navy: #0b3a66;
    --orange: #f6921e;
    --orange-deep: #e8561f;
    --yellow: #fdd835;
    --cream: #fffbe3;
    --white: #ffffff;
    --stage: #a4a4a4;
  }
  * { margin: 0; padding: 0; box-sizing: border-box; }
  html, body { width: 1200px; height: 1200px; overflow: hidden; }
  body { background: var(--stage); font-family: "Montserrat", sans-serif; }

  .flyer {
    position: absolute; left: 180px; top: 6px;
    width: 840px; height: 1188px;
    background: var(--white); overflow: hidden;
  }
  .soft-glow {
    position: absolute; left: -120px; top: 60px; width: 420px; height: 420px;
    border-radius: 50%; background: var(--cream);
  }
  .flame-sweep {
    position: absolute; left: 260px; top: 0; width: 580px; height: 330px;
    background: linear-gradient(200deg, var(--orange) 0%, var(--yellow) 45%, rgba(255,240,170,0) 85%);
  }
  .speaker-photo {
    position: absolute; left: 530px; top: 140px; width: 310px; height: 938px;
    background: linear-gradient(160deg, #d9633a 0%, #e4552a 40%, #c9451f 65%, #2c3d78 100%);
  }

  .brand {
    position: absolute; left: 48px; top: 150px;
    display: flex; align-items: center; gap: 12px;
  }
  .brand-dot { width: 34px; height: 34px; border-radius: 50%; background: var(--orange); }
  .brand-name {
    font-family: "Montserrat", sans-serif; font-weight: 600;
    font-size: 56px; letter-spacing: 2px; color: var(--navy);
  }

  .headline-disc {
    position: absolute; left: 20px; top: 260px; width: 560px; height: 560px;
    border-radius: 50%; background: var(--orange);
  }
  .headline {
    position: absolute; left: 95px; top: 345px; width: 440px; color: var(--white);
  }
  .event-name {
    font-family: "Oswald", sans-serif; font-weight: 700;
    font-size: 118px; line-height: 1; letter-spacing: 1px;
  }
  .event-sub {
    font-family: "Oswald", sans-serif; font-weight: 700;
    font-size: 58px; line-height: 1.05; color: var(--navy); margin-top: 2px;
  }
  .theme {
    font-family: "Montserrat", sans-serif; font-weight: 800;
    font-size: 37px; margin-top: 18px;
  }
  .focus-list { display: flex; gap: 16px; margin-top: 14px; }
  .focus-item {
    display: flex; align-items: center; gap: 7px;
    font-family: "Oswald", sans-serif; font-weight: 700; font-size: 20px;
  }
  .focus-icon {
    width: 40px; height: 40px; border-radius: 50%;
    border: 3px solid var(--navy); background: var(--orange);
    display: flex; align-items: center; justify-content: center;
  }
  .speaker-label {
    font-family: "Montserrat", sans-serif; font-weight: 800;
    font-size: 27px; margin-top: 22px; line-height: 1;
  }
  .speaker-name {
    font-family: "Montserrat", sans-serif; font-weight: 800;
    font-size: 27px; color: var(--navy); line-height: 1.2; white-space: nowrap;
  }

  .schedule {
    position: absolute; left: 160px; top: 838px;
    border-collapse: collapse; background: var(--white);
    font-family: "Oswald", sans-serif; font-weight: 500; font-size: 23px; color: var(--navy);
  }
  .schedule td { border: 1.5px solid var(--navy); padding: 3px 12px; white-space: nowrap; }
  .schedule .time { text-align: center; }

  .venue {
    position: absolute; left: 170px; top: 1000px;
    font-family: "Montserrat", sans-serif; font-style: normal;
    font-size: 20px; line-height: 1.2; color: #1b1b1b; white-space: nowrap;
  }
  .venue-name { color: var(--navy); font-weight: 700; }

  .contact-band {
    position: absolute; left: 0; bottom: 0; width: 840px; height: 110px;
    background: var(--navy);
    display: flex; align-items: center; justify-content: space-between; padding: 0 26px;
  }
  .contact-item {
    display: flex; align-items: center; gap: 10px; white-space: nowrap;
    color: var(--white); font-weight: 500; font-size: 17px;
  }
  .contact-item.phone { font-size: 23px; }
  .contact-icon {
    flex: none; width: 40px; height: 40px; border-radius: 50%;
    border: 2.5px solid var(--orange);
    display: flex; align-items: center; justify-content: center;
  }
</style>
</head>
<body>
  <main class="flyer">
    <div class="soft-glow"></div>
    <div class="flame-sweep" role="img" aria-label="Sweeping yellow and orange flame swirls"></div>
    <div class="speaker-photo" role="img" aria-label="Photo of the speaker seated in an orange blazer, glasses and a patterned tie"></div>

    <div class="brand">
      <span class="brand-dot"></span>
      <span class="brand-name">VANTRE</span>
    </div>

    <div class="headline-disc"></div>
    <div class="headline">
      <div class="event-name">KESTREL</div>
      <div class="event-sub">SUMMIT 2020</div>
      <div class="theme">In Fire and On Fire</div>
      <div class="focus-list">
        <div class="focus-item">
          <span class="focus-icon">
            <svg width="18" height="22" viewBox="0 0 18 22"><path d="M9 1C11 6 16 8 16 14a7 7 0 0 1-14 0c0-4 3-5 3-9 2 2 3 4 3 6 1-2 1-6 1-10z" fill="#fff"/></svg>
          </span>FIRE
        </div>
        <div class="focus-item">
          <span class="focus-icon">
            <svg width="22" height="22" viewBox="0 0 22 22"><path d="M11 2l8 9-8 9-8-9z" fill="none" stroke="#fff" stroke-width="2"/><path d="M11 2v18M3 11h16" stroke="#fff" stroke-width="1.5"/></svg>
          </span>REVIVAL
        </div>
        <div class="focus-item">
          <span class="focus-icon">
            <svg width="22" height="18" viewBox="0 0 22 18"><path d="M2 16c2-8 6-12 9-12s7 4 9 12" fill="none" stroke="#fff" stroke-width="2.5"/><circle cx="11" cy="11" r="3" fill="#fff"/></svg>
          </span>PROPHETIC
        </div>
      </div>
      <div class="speaker-label">SPEAKER:</div>
      <div class="speaker-name">PROPHET MARCUS OLUNDE</div>
    </div>

    <table class="schedule">
      <tr><td>Thursday</td><td>December 31st</td><td class="time">6:30PM</td></tr>
      <tr><td>Friday</td><td>January 1st</td><td class="time">6:30PM</td></tr>
      <tr><td>Saturday</td><td>January 2nd</td><td class="time">6:30PM</td></tr>
      <tr><td>Sunday</td><td>January 3rd</td><td class="time">4:30PM</td></tr>
    </table>

    <address class="venue">
      <div class="venue-name">Harlow Community Center</div>
      <div>239 Fennimore Street</div>
      <div>Portland, ME 04117</div>
    </address>

    <footer class="contact-band">
      <div class="contact-item phone">
        <span class="contact-icon">
          <svg width="20" height="20" viewBox="0 0 20 20"><path d="M4 2l4 1 1 4-2 2c1 2 3 4 5 5l2-2 4 1 1 4-2 2C9 18 2 11 2 4z" fill="#f6921e"/></svg>
        </span>207 583 2914
      </div>
      <div class="contact-item">
        <span class="contact-icon">
          <svg width="20" height="16" viewBox="0 0 20 16"><rect x="1" y="1" width="18" height="14" fill="none" stroke="#f6921e" stroke-width="2"/><path d="M1 1l9 8 9-8" fill="none" stroke="#f6921e" stroke-width="2"/></svg>
        </span>contact@brightmeadowfold.org
      </div>
      <div class="contact-item">
        <span class="contact-icon">
          <svg width="20" height="20" viewBox="0 0 20 20"><circle cx="10" cy="10" r="8" fill="none" stroke="#f6921e" stroke-width="2"/><ellipse cx="10" cy="10" rx="3.5" ry="8" fill="none" stroke="#f6921e" stroke-width="1.5"/><path d="M2 10h16" stroke="#f6921e" stroke-width="1.5"/></svg>
        </span>www.vantre.org
      </div>
    </footer>
  </main>
</body>
</html>
```